Voravolt Sports Performance Poster

We are in need of a poster for our upcoming summer Sports Performance Program during June and July.
This program caters to youth and teen athletes playing volleyball, soccer, and basketball.
Please see attached word document with program details for the poster.

MUST HAVES:
- Size needed 11x17 with bleeding for printing
- .PSD File Format WITH LAYERS (CS3 Compatible - Fonts included)*** A MUST
- Use Voravolt Bootcamps Logo
- Use Information in the attached word doc

Requirements
Must have
• - Size needed 11x17 with bleeding for printing
• - .PSD File Format WITH LAYERS (CS3 Compatible - Fonts included)*** A MUST
• - Use Voravolt Bootcamps Logo
• - Use Information in the attached word doc

```html
<!DOCTYPE html>
<html lang="en">
<head>
<meta charset="utf-8">
<title>Voravolt Sports Performance Program Poster</title>
<link rel="stylesheet" href="https://fonts.googleapis.com/css2?family=Bebas+Neue&family=Roboto:wght@300&display=swap">
<style>
  :root {
    --page: #e4e1dc;
    --ink: #000000;
    --red: #c8161d;
    --band-red: #b3161b;
    --white: #ffffff;
    --soft-white: #e2e2e2;
    --hero-skin: #5a3424;
    --hero-ball: #a8461f;
    --photo-grass: #4f7a2b;
    --photo-court: #b28e55;
  }
  html, body {
    margin: 0;
    width: 1200px;
    height: 1200px;
    overflow: hidden;
    background: var(--page);
  }
  .poster {
    position: absolute;
    left: 160px;
    top: 30px;
    width: 968px;
    height: 1252px;
    transform: scale(0.91);
    transform-origin: top left;
    background: var(--ink);
    overflow: hidden;
    font-family: "Bebas Neue", "Oswald", sans-serif;
    color: var(--white);
  }
  .poster > * { position: absolute; margin: 0; line-height: 1; white-space: nowrap; }
  .tagline {
    top: 16px; left: 0; width: 100%; text-align: center;
    font-family: "Roboto", sans-serif; font-weight: 300;
    font-size: 37px; letter-spacing: 1px; word-spacing: 6px;
  }
  .hero {
    left: 150px; top: 60px; width: 660px; height: 420px;
    background: radial-gradient(ellipse 42% 36% at 68% 72%, var(--hero-ball) 0%, rgba(120,50,25,.55) 45%, transparent 75%),
                radial-gradient(ellipse 55% 60% at 50% 40%, var(--hero-skin) 0%, rgba(40,22,16,.6) 50%, transparent 80%);
  }
  .brand-title {
    top: 440px; left: 0; width: 100%; text-align: center;
    font-size: 118px; color: var(--red); letter-spacing: 1px;
  }
  .program-title {
    top: 566px; left: 0; width: 100%; text-align: center;
    font-size: 72px; color: var(--soft-white); word-spacing: 10px;
  }
  .layout-shapes { top: 0; left: 0; }
  .ages { top: 668px; left: 39px; font-size: 52px; }
  .programs { top: 722px; left: 39px; font-size: 32px; }
  .dates { top: 674px; left: 426px; font-size: 38px; text-align: right; line-height: 1.2; }
  .schedule { top: 664px; right: 22px; font-size: 21px; text-align: right; line-height: 1.24; }
  .schedule span { display: block; }
  .schedule .s2 { margin-right: 68px; }
  .schedule .s3 { margin-right: 90px; }
  .schedule .s4 { margin-right: 134px; }
  .price { top: 1124px; left: 39px; font-size: 56px; }
  .price small { font-size: 29px; }
  .capacity { top: 1184px; left: 39px; font-size: 38px; }
  .brand-mark { top: 1136px; left: 664px; width: 270px; text-align: center; }
  .brand-mark .name { font-size: 40px; display: block; }
  .brand-mark .sub { font-size: 17px; letter-spacing: 1px; display: block; margin-top: 4px; }
</style>
</head>
<body>
<main class="poster">
  <p class="tagline">SPEED &ndash; AGILITY &ndash; POWER</p>
  <div class="hero" role="img" aria-label="Athlete in a dark jersey holding a basketball against a black background"></div>
  <h1 class="brand-title">VORAVOLT&rsquo;S</h1>
  <h2 class="program-title">SPORTS PERFORMANCE PROGRAM</h2>

  <svg class="layout-shapes" width="968" height="1252" viewBox="0 0 968 1252">
    <rect class="band" x="0" y="637" width="968" height="16" fill="var(--band-red)"/>
    <polygon class="divider" points="420,653 442,653 372,768 350,768" fill="var(--band-red)"/>
    <rect class="band" x="0" y="768" width="968" height="17" fill="var(--band-red)"/>
    <g class="photo-strip">
      <polygon points="0,785 110,785 -40,1078 0,1078" fill="var(--photo-court)" role="img" aria-label="Basketball hoop and net"/>
      <polygon points="132,785 355,785 205,1078 -18,1078" fill="var(--photo-grass)" role="img" aria-label="Girl in red kicking a soccer ball on a field"/>
      <polygon points="377,785 600,785 450,1078 227,1078" fill="#8a6a4a" role="img" aria-label="Volleyball players jumping at the net"/>
      <polygon points="622,785 855,785 705,1078 472,1078" fill="var(--photo-grass)" role="img" aria-label="Soccer player in white running with the ball"/>
      <polygon points="877,785 968,785 968,1078 727,1078" fill="#6b5a3c" role="img" aria-label="Basketball player rising toward the hoop"/>
      <g fill="var(--band-red)">
        <polygon points="110,785 132,785 -18,1078 -40,1078"/>
        <polygon points="355,785 377,785 227,1078 205,1078"/>
        <polygon points="600,785 622,785 472,1078 450,1078"/>
        <polygon points="855,785 877,785 727,1078 705,1078"/>
      </g>
    </g>
    <rect class="band" x="0" y="1078" width="968" height="17" fill="var(--band-red)"/>
  </svg>

  <p class="ages">AGES 8-17</p>
  <p class="programs">YOUTH AND TEEN PROGRAMS</p>
  <p class="dates">JUNE 5TH &ndash; 30TH<br>JULY 5TH &ndash; 31ST</p>
  <p class="schedule">
    <span class="s1">MONDAY, WEDNESDAY, FRIDAY</span>
    <span class="s2">YOUTH &ndash; 9:30-10:30AM</span>
    <span class="s3">TEEN &ndash; 10:30-11:30AM</span>
    <span class="s4">TEEN &ndash; 3:30-4:30PM</span>
  </p>
  <p class="price">$119 <small>PER MONTH OR</small> $199 <small>FOR BOTH MONTHS</small></p>
  <p class="capacity">LIMITED SPACE &ndash; 15 SPOTS PER TIME TRACK</p>
  <p class="brand-mark"><span class="name">VORAVOLT BOOTCAMPS</span><span class="sub">THE ULTIMATE FITNESS SOLUTION</span></p>
</main>
</body>
</html>
```